The Willow Compass

Look for someone who can add some splash and make this powerpoint presentation more dynamic. Feel free to use color, animations etc to provide some punch.

```html
<!DOCTYPE html>
<html lang="en">
<head>
<meta charset="utf-8">
<title>The Willow Compass – Course Deck</title>
<link href="https://fonts.googleapis.com/css2?family=Montserrat:wght@400;500;600;700;800&display=swap" rel="stylesheet">
<style>
:root{
  --navy:#2c4a76;
  --blue:#3f6aa6;
  --ink:#2f3e57;
  --sky:#a9c4e6;
  --pale:#dce8f5;
  --white:#ffffff;
  --canvas:#000000;
  --rule:#e3e8ef;
}
*{margin:0;padding:0;box-sizing:border-box}
html,body{width:1200px;height:4481px;overflow:hidden;background:var(--canvas)}
body{font-family:"Montserrat",sans-serif;color:var(--ink);position:relative}
.slide{position:absolute;left:80px;width:1040px;height:584px;background:var(--white);overflow:hidden}
.slide::before{content:"";position:absolute;left:0;top:0;width:860px;height:8px;background:var(--sky);clip-path:polygon(0 0,100% 0,98% 100%,0 100%);z-index:3}
.s1{top:70px}.s2{top:696px}.s3{top:1322px}.s4{top:1948px}.s5{top:2574px}.s6{top:3200px}.s7{top:3826px}
.abs{position:absolute}
.heading{font-weight:800;color:var(--navy);text-transform:uppercase;line-height:1.12;letter-spacing:.3px}
.on-dark{color:var(--white)}
.bullets{list-style:none}
.bullets li{position:relative;padding-left:20px;font-size:12.5px;line-height:1.35;margin-bottom:13px}
.bullets li::before{content:"";position:absolute;left:0;top:3px;width:10px;height:10px;border-radius:50%;background:var(--blue);
  -webkit-mask:radial-gradient(circle,transparent 2px,#000 2.5px);mask:radial-gradient(circle,transparent 2px,#000 2.5px)}
.bullets.light li{color:var(--white)}
.bullets.light li::before{background:var(--white)}
.photo{position:absolute}
.brand{font-weight:500;color:var(--navy);letter-spacing:3px;text-transform:uppercase;display:flex;align-items:center;gap:12px;white-space:nowrap}
.brand .dot{flex:none;width:12px;height:12px;border-radius:50%;background:var(--blue)}
.illustration{position:absolute;border-radius:4px}
.title-main{left:58px;top:72px;font-size:33px}
.tagline{left:58px;top:162px;font-size:19px;font-weight:500;color:var(--blue);line-height:1.2}
.module-title{left:0;width:100%;top:58px;text-align:center;font-size:32px}
.lessons{left:59px;top:192px;width:930px;display:grid;grid-template-columns:repeat(3,283px);column-gap:38px}
.lesson{display:flex;align-items:center;gap:18px;height:85px;border-bottom:1px solid var(--rule);font-size:12.5px;line-height:1.3}
.lesson:nth-last-child(-n+3){border-bottom:none}
.chev{flex:none;width:34px;height:34px;border-radius:50%;background:var(--blue);display:flex;align-items:center;justify-content:center}
.contact{display:flex;align-items:center;gap:22px;padding:18px 0;border-bottom:1px solid var(--rule);width:320px;font-size:16px;color:var(--navy);line-height:1.35}
.contact:last-child{border-bottom:none}
.contact .ico{flex:none;width:42px;height:42px;border-radius:50%;background:var(--blue);display:flex;align-items:center;justify-content:center}
</style>
</head>
<body>

<!-- 1 Cover -->
<section class="slide s1">
  <h1 class="abs heading title-main">The Willow<br>Compass</h1>
  <p class="abs tagline">How to raise faster,<br>get back to building<br>and grow</p>
  <div class="abs brand" style="left:640px;top:172px;font-size:20px"><span class="dot"></span>Harbor Lane Partners</div>
  <div class="illustration" role="img" aria-label="Illustrated blue mountain range with a dotted pink route climbing to a flag at the summit"
       style="left:100px;top:250px;width:870px;height:334px;background:linear-gradient(180deg,var(--pale) 0%,var(--sky) 30%,var(--blue) 65%,var(--navy) 100%)"></div>
</section>

<!-- 2 Module index -->
<section class="slide s2">
  <h2 class="abs heading module-title">Module One<br>The Fundraising Journey</h2>
  <div class="abs lessons">
    <div class="lesson"><span class="chev"><svg width="12" height="12" viewBox="0 0 12 12"><path d="M4 2l4 4-4 4" stroke="#fff" stroke-width="2" fill="none"/></svg></span>Welcome</div>
    <div class="lesson"><span class="chev"><svg width="12" height="12" viewBox="0 0 12 12"><path d="M4 2l4 4-4 4" stroke="#fff" stroke-width="2" fill="none"/></svg></span>It's All About The Story</div>
    <div class="lesson"><span class="chev"><svg width="12" height="12" viewBox="0 0 12 12"><path d="M4 2l4 4-4 4" stroke="#fff" stroke-width="2" fill="none"/></svg></span>Where to find the accredited investors?</div>
    <div class="lesson"><span class="chev"><svg width="12" height="12" viewBox="0 0 12 12"><path d="M4 2l4 4-4 4" stroke="#fff" stroke-width="2" fill="none"/></svg></span>About Me &amp; My Background</div>
    <div class="lesson"><span class="chev"><svg width="12" height="12" viewBox="0 0 12 12"><path d="M4 2l4 4-4 4" stroke="#fff" stroke-width="2" fill="none"/></svg></span>Accelerators (Good/Bad/Maybe)</div>
    <div class="lesson"><span class="chev"><svg width="12" height="12" viewBox="0 0 12 12"><path d="M4 2l4 4-4 4" stroke="#fff" stroke-width="2" fill="none"/></svg></span>Unlocking the Power of Angel Investors</div>
    <div class="lesson"><span class="chev"><svg width="12" height="12" viewBox="0 0 12 12"><path d="M4 2l4 4-4 4" stroke="#fff" stroke-width="2" fill="none"/></svg></span>Why I created this course</div>
    <div class="lesson"><span class="chev"><svg width="12" height="12" viewBox="0 0 12 12"><path d="M4 2l4 4-4 4" stroke="#fff" stroke-width="2" fill="none"/></svg></span>Why Not Sand Hill Road?</div>
    <div class="lesson"><span class="chev"><svg width="12" height="12" viewBox="0 0 12 12"><path d="M4 2l4 4-4 4" stroke="#fff" stroke-width="2" fill="none"/></svg></span>Early-Stage Fundraising Traps</div>
    <div class="lesson"><span class="chev"><svg width="12" height="12" viewBox="0 0 12 12"><path d="M4 2l4 4-4 4" stroke="#fff" stroke-width="2" fill="none"/></svg></span>The Fundraising Journey</div>
    <div class="lesson"><span class="chev"><svg width="12" height="12" viewBox="0 0 12 12"><path d="M4 2l4 4-4 4" stroke="#fff" stroke-width="2" fill="none"/></svg></span>The different types of capital</div>
    <div class="lesson"><span class="chev"><svg width="12" height="12" viewBox="0 0 12 12"><path d="M4 2l4 4-4 4" stroke="#fff" stroke-width="2" fill="none"/></svg></span>The Easiest Money You Will Ever Raise</div>
  </div>
</section>

<!-- 3 About -->
<section class="slide s3">
  <div class="abs" style="left:0;top:0;width:449px;height:584px;background:var(--blue)"></div>
  <h2 class="abs heading on-dark" style="left:40px;top:120px;font-size:26px">About Me &amp; My<br>Background</h2>
  <ul class="abs bullets light" style="left:40px;top:198px;width:255px">
    <li>Over the last 25yrs, I helped two companies build business units to revenues over $1B annually.</li>
    <li>Then, in 2018, I burned out.</li>
    <li>So, I decided to leave the corporate executive grind to help early-stage founders.</li>
    <li>So, I started building my company and brand in 2018.</li>
    <li>Since that day, I've spent my time finding ways to help early-stage Founders win!</li>
  </ul>
  <div class="photo" role="img" aria-label="Portrait photo of the course author, a grey-haired man, in a white frame"
       style="left:333px;top:72px;width:250px;height:440px;border:3px solid #fff;background:linear-gradient(160deg,#3a3a3a,#1c1c1c 60%,#5b5b5b)"></div>
  <h2 class="abs heading" style="left:769px;top:152px;font-size:24px">My Results</h2>
  <ul class="abs bullets" style="left:769px;top:202px;width:240px">
    <li>64 companies invested in</li>
    <li>35 companies have gotten to Series A</li>
    <li>$1.08B+ capital raised by my portfolio companies</li>
    <li>8 exits to date</li>
    <li>Consulting business working with early-stage founders across 5 continents</li>
    <li>90% margins</li>
  </ul>
</section>

<!-- 4 Why -->
<section class="slide s4">
  <h2 class="abs heading" style="left:58px;top:75px;font-size:33px">Why I Created This<br>Course</h2>
  <p class="abs" style="left:58px;top:172px;font-size:19px;font-weight:500;line-height:1.25;color:var(--ink)">Spent 6 years chatting with over 3,000<br>founders and learned:</p>
  <ul class="abs bullets" style="left:58px;top:240px;width:480px">
    <li>The fundraising process is NOT transparent</li>
    <li>Founders don't know where to begin, who to talk to or where to start</li>
    <li>Founders don't get the candid feedback they need</li>
    <li>There is not easy way to find the right type of investors</li>
    <li>Founders don't always know what investors want, how to present it and the what the necessary KPI's for success are</li>
    <li>Founders underestimate how hard, long and tedious this process is start to finish</li>
    <li>The result is a fragmented, slow and challenging journey that leaves founders feeling empty and ultimately unfunded.</li>
  </ul>
  <div class="photo" role="img" aria-label="Office photo of a confident businessman in a navy suit with arms crossed, a colleague working at a laptop behind him"
       style="left:595px;top:0;width:445px;height:584px;background:linear-gradient(135deg,#c9d3dc,#8a98a6 45%,#24324a 100%)"></div>
</section>

<!-- 5 Expected results -->
<section class="slide s5">
  <div class="photo" role="img" aria-label="Photo of small trees growing on rising stacks of coins with a glowing upward arrow"
       style="left:0;top:0;width:447px;height:584px;background:linear-gradient(160deg,#2b2b2b,#4a5a3a 55%,#c9cfd6 100%)"></div>
  <h2 class="abs heading" style="left:522px;top:128px;font-size:33px">Expected Results for<br>Founders</h2>
  <ul class="abs bullets" style="left:522px;top:226px;width:440px">
    <li>Founders now have a firm understanding of the fundraising process end-to-end</li>
    <li>Founder have resources to help them find the right investors at the right time</li>
    <li>Founders understand the different types of investors, motivation and stages</li>
    <li>Founders understand how to tell their story more effectively</li>
    <li>Founders feel equipped to successfully raise capital from the right type of investors</li>
    <li>Founders reduce to fundraise from 6-8 months to 3-6 mths</li>
  </ul>
</section>

<!-- 6 Who -->
<section class="slide s6">
  <div class="abs" style="left:0;top:0;width:522px;height:584px;background:var(--blue)"></div>
  <h2 class="abs heading on-dark" style="left:40px;top:110px;font-size:26px">Who Is This<br>Course For?</h2>
  <ul class="abs bullets light" style="left:40px;top:190px;width:250px">
    <li>Early-Stage founders considering raising outside capital to fund their company.</li>
    <li>Founders looking to understand the fundraising process along with the players involved</li>
    <li>Founders who are looking to accelerate the capital raising process for their company.</li>
    <li>Founders who are looking to nail their ICP (Ideal Customer Profile) for investors</li>
    <li>Founders who are frustrated with how long and hard the fundraising process can be.</li>
  </ul>
  <div class="photo" role="img" aria-label="Photo of a smiling young woman in a beige blazer holding a tablet"
       style="left:346px;top:50px;width:348px;height:484px;background:linear-gradient(170deg,#eef1f4,#d8cbbb 55%,#b9a58e 100%)"></div>
  <h2 class="abs heading" style="left:753px;top:110px;font-size:26px">Who Isn't This<br>Course For?</h2>
  <ul class="abs bullets" style="left:753px;top:196px;width:240px">
    <li>Tire Kickers</li>
    <li>Wantrapreneurs vs Entrepreneurs</li>
    <li>Founders at Series A and beyond</li>
    <li>Founders who are not willing to do the work</li>
  </ul>
</section>

<!-- 7 Thank you -->
<section class="slide s7">
  <div class="abs brand" style="left:58px;top:150px;font-size:22px"><span class="dot"></span>Harbor Lane Partners</div>
  <h2 class="abs heading" style="left:58px;top:215px;font-size:32px">Thank You</h2>
  <div class="abs" style="left:58px;top:268px">
    <div class="contact">
      <span class="ico"><svg width="20" height="20" viewBox="0 0 24 24"><path fill="#fff" d="M6.6 10.8a15 15 0 006.6 6.6l2.2-2.2c.3-.3.7-.4 1-.2 1.1.4 2.3.6 3.6.6.6 0 1 .4 1 1V20c0 .6-.4 1-1 1A17 17 0 013 4c0-.6.4-1 1-1h3.5c.6 0 1 .4 1 1 0 1.3.2 2.5.6 3.6.1.3 0 .7-.2 1z"/></svg></span>
      <div>Phone<br>+1 555 0142 7788</div>
    </div>
    <div class="contact">
      <span class="ico"><svg width="18" height="20" viewBox="0 0 24 24"><path fill="#fff" d="M12 2a7 7 0 00-7 7c0 5 7 13 7 13s7-8 7-13a7 7 0 00-7-7zm0 9.5A2.5 2.5 0 1112 6.5a2.5 2.5 0 010 5z"/></svg></span>
      <div>Harbor Lane Partners<br>48 Birchwood Avenue</div>
    </div>
    <div class="contact">
      <span class="ico"><svg width="20" height="16" viewBox="0 0 24 18"><rect x="1" y="1" width="22" height="16" rx="2" fill="#fff"/><path d="M2 2l10 8 10-8" stroke="#3f6aa6" stroke-width="2" fill="none"/></svg></span>
      <div>Email<br>info@harborlanepartners.com</div>
    </div>
  </div>
  <div class="illustration" role="img" aria-label="Illustrated blue mountain with a dotted pink route climbing to a flag at the summit"
       style="left:560px;top:40px;width:480px;height:544px;background:linear-gradient(180deg,var(--pale) 0%,var(--sky) 35%,var(--blue) 65%,var(--navy) 100%)"></div>
</section>

</body>
</html>
```